Poster for Tradesmen Website

We had a soft launch of our website. The site brings together tradesmen jobseekers and customers to one virtual location. The website serves Australian market. To clearly understand what we mean please visit www.quellmark.com.au. For our future promotional campaign we intend to use poster which we intend to distribute in trade exhibits and in recruitment offices.
Color and Poster Design Content: - Very light blue is the predominant color of the website. The design is not limited on this color. They are free to explore other color if they think that will effectively convey the message of the poster. Presently our website uses images showing tradesmen in action as well as the customers. Designers can use these images or use other image in their design which will best suit their design
Size: - We are looking at poster printed A3 size, but the design should not limit their target size on A3 (it should be versatile, insure that the file format for your design support large-format printing without being pixilated) since we also want it printed in vinyl as stand-alone banner (example: 1200 x 1700 mm approx) that will be used in trade exhibits.
Message of the Poster:
For our first marketing campaign we want to join a trade expo which will be held on the last week of May 2012. For this expo we need a poster and a stand-alone banner to be displayed on our booth. The poster should convey the following message:
a) that a new website has been launched
b) that the website brings together tradesmen, customers and jobseekers to one virtual location
c) that for tradesmen the website is a venue to advertise their business
d) that for customers, it will make the task of finding the right tradies much easier
e) that for jobseekers the site is one way of finding a job by just posting their resume and potential employers can view the summary of their qualification and send notification if they are interested on a particular jobseeker.
Images:
We don't have any other high resolution images Except for the images that we used on our website. We got those images online. Besides, we are not sure what particular image will be appropriate for the poster. As the designer and the creative artist as well, you are free to use whatever images that you think is appropriate for the your design. We think any images (not necessarily tradesmen images) can be used as long as it can strongly convey our message. Again, as the creative artist it is up to you to decide what image is/are appropriate. The only thing we can tell you guys is that we can tell a good/excellent design when we see one.
Logo:
We don't have a logo yet for our website. For the purpose of this poster you can use the font used on website name:
quellmark.com.au
quell {font-family:Arial, Helvetica, sans-serif; color:#407FC0;}
mark.com.au {font-family:Arial, Helvetica, sans-serif; color:#00007F;}
Age group: 18 - 65, Gender: male-female, Education: any
Marketing

```html
<!DOCTYPE html>
<html lang="en">
<head>
<meta charset="utf-8">
<title>Brand New – quellmark.com.au</title>
<link href="https://fonts.googleapis.com/css2?family=Arvo:wght@400;700&family=Arimo:wght@400;700&display=swap" rel="stylesheet">
<style>
  :root {
    --navy: #2a1a6d;
    --sky: #7cc3ef;
    --panel-light: #3bb0ea;
    --panel-mid: #27a2e2;
    --panel-deep: #1d8fd0;
    --ink: #14202c;
    --white: #ffffff;
  }
  html, body {
    margin: 0;
    padding: 0;
    width: 848px;
    height: 1200px;
    overflow: hidden;
    background: var(--navy);
  }
  .poster {
    position: relative;
    width: 848px;
    height: 1200px;
    background: var(--navy);
    font-family: "Arvo", "Rockwell", serif;
  }
  .headline {
    position: absolute;
    left: 0;
    width: 848px;
    text-align: center;
    margin: 0;
  }
  .headline__launch {
    top: 38px;
    font-size: 58px;
    font-weight: 700;
    letter-spacing: 4px;
    color: var(--sky);
  }
  .headline__url {
    top: 106px;
    font-family: "Arimo", Arial, sans-serif;
    font-size: 43px;
    font-weight: 400;
    color: var(--white);
  }
  .headline__tagline {
    top: 163px;
    font-size: 37px;
    font-weight: 700;
    letter-spacing: 3.2px;
    color: var(--sky);
  }
  .feature-panel {
    position: absolute;
    left: 118px;
    top: 243px;
    width: 612px;
    height: 821px;
    overflow: hidden;
  }
  .feature-panel__photo {
    position: absolute;
    inset: 0;
    background: radial-gradient(ellipse at 50% 55%, var(--panel-light) 0%, var(--panel-mid) 55%, var(--panel-deep) 100%);
  }
  .feature-panel__numerals {
    position: absolute;
    inset: 0;
  }
  .feature-panel__numerals text {
    font-family: "Arimo", Arial, sans-serif;
    font-weight: 700;
    font-size: 380px;
    fill: none;
    stroke: var(--white);
    stroke-width: 1.2;
  }
  .benefit {
    position: absolute;
    margin: 0;
    font-size: 30px;
    font-weight: 700;
    line-height: 42.5px;
    color: var(--ink);
  }
  .benefit--left { left: 49px; text-align: left; }
  .benefit--right { right: 54px; text-align: right; }
  .benefit--one { top: 38px; }
  .benefit--two { top: 262px; }
  .benefit--three { top: 446px; }
  .benefit--four { top: 640px; }
  .contact-line {
    position: absolute;
    left: 0;
    top: 1094px;
    width: 848px;
    margin: 0;
    text-align: center;
    font-size: 30px;
    font-weight: 400;
    letter-spacing: 2.6px;
    color: var(--white);
  }
</style>
</head>
<body>
<main class="poster">
  <h1 class="headline headline__launch">Brand New</h1>
  <p class="headline headline__url">https://www.quellmark.com.au</p>
  <p class="headline headline__tagline">website for great jobs</p>

  <section class="feature-panel">
    <div class="feature-panel__photo" role="img" aria-label="Circle of smiling tradespeople and customers seen from below, tinted blue"></div>
    <svg class="feature-panel__numerals" width="612" height="821" viewBox="0 0 612 821" aria-hidden="true">
      <text x="-30" y="270">1</text>
      <text x="385" y="388">2</text>
      <text x="-6" y="628">3</text>
      <text x="370" y="812">4</text>
    </svg>
    <p class="benefit benefit--left benefit--one">brings together<br>tradesmen,<br>customers and<br>job seekers</p>
    <p class="benefit benefit--right benefit--two">finding<br>the right trades<br>much easier</p>
    <p class="benefit benefit--left benefit--three">just post resume &amp;<br>potential employers<br>will find you</p>
    <p class="benefit benefit--right benefit--four">best venue<br>to advertise<br>your business</p>
  </section>

  <p class="contact-line">Questions? Call 1-800-555-0148</p>
</main>
</body>
</html>
```